Pest Control Company needs business card!

Hi there, we need a business card designed for our new Pest Control Company. Ideally this card will be simple, yet feel elegant and high end. We want to use the colours Orange, Black and White. Please see our attached logo for the exact colours.

Business card details:

Phone - 0461 275 804
Name - Gavin Holloway
Email - Info@steadfastverminguard.com.au

We would also like to include the following list with dot points:

SERVICES / INSPECTIONS

Termites, Wood Borers, Ants, Cockroaches, Spiders, Fleas, Mice, Rats, Bed Bugs, & More!

```html
<!DOCTYPE html>
<html lang="en">
<head>
<meta charset="utf-8">
<title>Steadfast Vermin Guard – Business Card</title>
<link href="https://fonts.googleapis.com/css2?family=Montserrat:wght@500;700;800&display=swap" rel="stylesheet">
<style>
  :root {
    --orange: #f47f20;
    --orange-deep: #ee6f13;
    --black: #1d1d1d;
    --white: #ffffff;
    --stage: #2b2e33;
    --ink: #111111;
  }
  * { margin: 0; padding: 0; box-sizing: border-box; }
  html, body { width: 1200px; height: 900px; overflow: hidden; }
  body {
    background: var(--stage);
    font-family: "Montserrat", sans-serif;
    display: flex;
    flex-direction: column;
    align-items: center;
    justify-content: center;
    gap: 60px;
  }
  .card {
    position: relative;
    width: 600px;
    height: 345px;
    background: var(--white);
    border-radius: 22px;
    overflow: hidden;
  }
  .card-shapes { position: absolute; inset: 0; width: 100%; height: 100%; }

  /* Front */
  .brand {
    position: absolute;
    display: flex;
    align-items: center;
    gap: 12px;
    color: var(--ink);
    font-weight: 800;
    text-transform: uppercase;
    line-height: 1;
  }
  .brand-mark { border-radius: 50%; background: currentColor; flex: none; }
  .brand-front { left: 300px; top: 130px; font-size: 34px; }
  .brand-front .brand-mark { width: 46px; height: 46px; }
  .brand-front .brand-name span { display: block; }

  /* Back */
  .services { position: absolute; left: 36px; top: 34px; color: var(--ink); }
  .services-title { font-size: 15px; font-weight: 700; letter-spacing: .02em; margin-bottom: 10px; }
  .services-list { list-style: none; font-size: 13px; font-weight: 700; text-transform: uppercase; line-height: 21px; }
  .services-list li::before { content: "\25AA"; margin-right: 6px; }

  .brand-back { right: 26px; top: 146px; color: var(--white); font-size: 13px; gap: 7px; }
  .brand-back .brand-mark { width: 18px; height: 18px; }
  .brand-back .brand-name span { display: block; }

  .holder {
    position: absolute; left: 300px; top: 210px;
    color: var(--white); font-weight: 800; font-size: 30px; line-height: 1.05;
    text-transform: uppercase;
  }
  .contact { position: absolute; left: 262px; top: 280px; color: var(--white); font-size: 13px; font-weight: 500; }
  .contact-row { display: flex; align-items: center; gap: 8px; margin-bottom: 8px; }
  .contact-row.email { text-transform: uppercase; font-size: 11.5px; }
  .contact-icon { width: 14px; height: 14px; fill: var(--white); flex: none; }
</style>
</head>
<body>

  <section class="card card-front" aria-label="Business card front">
    <svg class="card-shapes" viewBox="0 0 600 345" preserveAspectRatio="none" aria-hidden="true">
      <polygon points="0,0 250,0 110,345 0,345" fill="var(--orange)"/>
      <polygon points="250,0 292,0 211,200 169,200" fill="var(--black)"/>
    </svg>
    <div class="brand brand-front">
      <div class="brand-name"><span>Steadfast</span><span>Vermin Guard</span></div>
      <span class="brand-mark"></span>
    </div>
  </section>

  <section class="card card-back" aria-label="Business card back">
    <svg class="card-shapes" viewBox="0 0 600 345" preserveAspectRatio="none" aria-hidden="true">
      <polygon points="310,152 600,120 600,92 345,124" fill="var(--black)"/>
      <polygon points="190,165 600,120 600,345 240,345" fill="var(--orange)"/>
    </svg>

    <div class="services">
      <h2 class="services-title">SERVICES / INSPECTIONS</h2>
      <ul class="services-list">
        <li>Termites</li>
        <li>Wood Borers</li>
        <li>Ants</li>
        <li>Cockroaches</li>
        <li>Spiders</li>
        <li>Fleas</li>
        <li>Mice</li>
        <li>Rats</li>
        <li>Bed Bugs &amp; More!</li>
      </ul>
    </div>

    <div class="brand brand-back">
      <div class="brand-name"><span>Steadfast</span><span>Vermin Guard</span></div>
      <span class="brand-mark"></span>
    </div>

    <p class="holder">Gavin<br>Holloway</p>

    <div class="contact">
      <p class="contact-row phone">
        <svg class="contact-icon" viewBox="0 0 24 24" aria-hidden="true"><path d="M6.6 10.8a15.1 15.1 0 0 0 6.6 6.6l2.2-2.2a1 1 0 0 1 1-.25 11.4 11.4 0 0 0 3.6.57 1 1 0 0 1 1 1V20a1 1 0 0 1-1 1A17 17 0 0 1 3 4a1 1 0 0 1 1-1h3.5a1 1 0 0 1 1 1c0 1.25.2 2.45.57 3.57a1 1 0 0 1-.25 1z"/></svg>
        0461 275 804
      </p>
      <p class="contact-row email">
        <svg class="contact-icon" viewBox="0 0 24 24" aria-hidden="true"><path d="M2 5h20v14H2zm2 2v.4l8 5.2 8-5.2V7zm0 2.8V17h16V9.8l-8 5.2z"/></svg>
        Info@steadfastverminguard.com.au
      </p>
    </div>
  </section>

</body>
</html>
```